Step and Repeat Backdrop for wedding reception photo booth

Would like to have a Step and Repeat Backdrop (8 foot high by 10 foot wide) that incorporates the wedding logo (attached) and the names Elena and Gavin. Background should be white, and wedding colors are burgundy and gold. Show me creativity :-) I have included some random samples.

```html
<!DOCTYPE html>
<html lang="en">
<head>
<meta charset="utf-8">
<title>Elena and Gavin – Step and Repeat Backdrop</title>
<link href="https://fonts.googleapis.com/css2?family=Marcellus&display=swap" rel="stylesheet">
<style>
  :root {
    --backdrop-white: #ffffff;
    --wedding-gold: #c8961e;
    --wedding-burgundy: #b0284f;
  }
  html, body {
    margin: 0;
    padding: 0;
    width: 1200px;
    height: 900px;
    overflow: hidden;
    background: var(--backdrop-white);
  }
  .backdrop {
    box-sizing: border-box;
    width: 1200px;
    height: 900px;
    padding: 40px 50px;
    display: grid;
    grid-template-columns: repeat(9, 1fr);
    grid-template-rows: repeat(6, 1fr);
    align-items: center;
    justify-items: center;
    font-family: "Marcellus", serif;
  }
  .wedding-mark {
    display: flex;
    flex-direction: column;
    align-items: center;
    gap: 6px;
    color: var(--wedding-gold);
  }
  .wedding-mark__dot {
    width: 26px;
    height: 26px;
    border-radius: 50%;
    background: var(--wedding-gold);
  }
  .wedding-mark__name {
    font-size: 17px;
    line-height: 1.15;
    text-align: center;
  }
  .couple-names {
    margin: 0;
    color: var(--wedding-burgundy);
    font-size: 20px;
    line-height: 1.2;
    text-align: center;
    text-transform: uppercase;
    letter-spacing: 0.5px;
  }
</style>
</head>
<body>
<main class="backdrop">
  <div class="wedding-mark"><span class="wedding-mark__dot"></span><span class="wedding-mark__name">Elena &amp;<br>Gavin</span></div><p class="couple-names">Elena<br>and<br>Gavin</p>
  <div class="wedding-mark"><span class="wedding-mark__dot"></span><span class="wedding-mark__name">Elena &amp;<br>Gavin</span></div><p class="couple-names">Elena<br>and<br>Gavin</p>
  <div class="wedding-mark"><span class="wedding-mark__dot"></span><span class="wedding-mark__name">Elena &amp;<br>Gavin</span></div><p class="couple-names">Elena<br>and<br>Gavin</p>
  <div class="wedding-mark"><span class="wedding-mark__dot"></span><span class="wedding-mark__name">Elena &amp;<br>Gavin</span></div><p class="couple-names">Elena<br>and<br>Gavin</p>
  <div class="wedding-mark"><span class="wedding-mark__dot"></span><span class="wedding-mark__name">Elena &amp;<br>Gavin</span></div>

  <div class="wedding-mark"><span class="wedding-mark__dot"></span><span class="wedding-mark__name">Elena &amp;<br>Gavin</span></div><p class="couple-names">Elena<br>and<br>Gavin</p>
  <div class="wedding-mark"><span class="wedding-mark__dot"></span><span class="wedding-mark__name">Elena &amp;<br>Gavin</span></div><p class="couple-names">Elena<br>and<br>Gavin</p>
  <div class="wedding-mark"><span class="wedding-mark__dot"></span><span class="wedding-mark__name">Elena &amp;<br>Gavin</span></div><p class="couple-names">Elena<br>and<br>Gavin</p>
  <div class="wedding-mark"><span class="wedding-mark__dot"></span><span class="wedding-mark__name">Elena &amp;<br>Gavin</span></div><p class="couple-names">Elena<br>and<br>Gavin</p>
  <div class="wedding-mark"><span class="wedding-mark__dot"></span><span class="wedding-mark__name">Elena &amp;<br>Gavin</span></div>

  <div class="wedding-mark"><span class="wedding-mark__dot"></span><span class="wedding-mark__name">Elena &amp;<br>Gavin</span></div><p class="couple-names">Elena<br>and<br>Gavin</p>
  <div class="wedding-mark"><span class="wedding-mark__dot"></span><span class="wedding-mark__name">Elena &amp;<br>Gavin</span></div><p class="couple-names">Elena<br>and<br>Gavin</p>
  <div class="wedding-mark"><span class="wedding-mark__dot"></span><span class="wedding-mark__name">Elena &amp;<br>Gavin</span></div><p class="couple-names">Elena<br>and<br>Gavin</p>
  <div class="wedding-mark"><span class="wedding-mark__dot"></span><span class="wedding-mark__name">Elena &amp;<br>Gavin</span></div><p class="couple-names">Elena<br>and<br>Gavin</p>
  <div class="wedding-mark"><span class="wedding-mark__dot"></span><span class="wedding-mark__name">Elena &amp;<br>Gavin</span></div>

  <div class="wedding-mark"><span class="wedding-mark__dot"></span><span class="wedding-mark__name">Elena &amp;<br>Gavin</span></div><p class="couple-names">Elena<br>and<br>Gavin</p>
  <div class="wedding-mark"><span class="wedding-mark__dot"></span><span class="wedding-mark__name">Elena &amp;<br>Gavin</span></div><p class="couple-names">Elena<br>and<br>Gavin</p>
  <div class="wedding-mark"><span class="wedding-mark__dot"></span><span class="wedding-mark__name">Elena &amp;<br>Gavin</span></div><p class="couple-names">Elena<br>and<br>Gavin</p>
  <div class="wedding-mark"><span class="wedding-mark__dot"></span><span class="wedding-mark__name">Elena &amp;<br>Gavin</span></div><p class="couple-names">Elena<br>and<br>Gavin</p>
  <div class="wedding-mark"><span class="wedding-mark__dot"></span><span class="wedding-mark__name">Elena &amp;<br>Gavin</span></div>

  <div class="wedding-mark"><span class="wedding-mark__dot"></span><span class="wedding-mark__name">Elena &amp;<br>Gavin</span></div><p class="couple-names">Elena<br>and<br>Gavin</p>
  <div class="wedding-mark"><span class="wedding-mark__dot"></span><span class="wedding-mark__name">Elena &amp;<br>Gavin</span></div><p class="couple-names">Elena<br>and<br>Gavin</p>
  <div class="wedding-mark"><span class="wedding-mark__dot"></span><span class="wedding-mark__name">Elena &amp;<br>Gavin</span></div><p class="couple-names">Elena<br>and<br>Gavin</p>
  <div class="wedding-mark"><span class="wedding-mark__dot"></span><span class="wedding-mark__name">Elena &amp;<br>Gavin</span></div><p class="couple-names">Elena<br>and<br>Gavin</p>
  <div class="wedding-mark"><span class="wedding-mark__dot"></span><span class="wedding-mark__name">Elena &amp;<br>Gavin</span></div>

  <div class="wedding-mark"><span class="wedding-mark__dot"></span><span class="wedding-mark__name">Elena &amp;<br>Gavin</span></div><p class="couple-names">Elena<br>and<br>Gavin</p>
  <div class="wedding-mark"><span class="wedding-mark__dot"></span><span class="wedding-mark__name">Elena &amp;<br>Gavin</span></div><p class="couple-names">Elena<br>and<br>Gavin</p>
  <div class="wedding-mark"><span class="wedding-mark__dot"></span><span class="wedding-mark__name">Elena &amp;<br>Gavin</span></div><p class="couple-names">Elena<br>and<br>Gavin</p>
  <div class="wedding-mark"><span class="wedding-mark__dot"></span><span class="wedding-mark__name">Elena &amp;<br>Gavin</span></div><p class="couple-names">Elena<br>and<br>Gavin</p>
  <div class="wedding-mark"><span class="wedding-mark__dot"></span><span class="wedding-mark__name">Elena &amp;<br>Gavin</span></div>
</main>
</body>
</html>
```